Business card design for modern LaneScope agency

Hello,

I need a business card design for my company Harbor9Studio.
We mainly offer Vornix LaneScope Tours (360° Photography) and it should be a business card with following details:

Name: Tobias Merland
Number: +49 160 55 82 907
Mail: tobias@harbor9studio.example
website: harbor9studio.example

Main colour that we use is the red of the logo.
It´s also important to integrate the "Vornix Gold logo" as the person on this business card is a Vornix Gold photographer.

And if possible we would also like to integrate something like send us a sms or pingwell and we call you back. As the number is german but we sell now in Vienna, Austria.

We offer a good price but very high photography quality, as we are mostly students - that´s our concept.

Maybe an idea is to integrate something 360° on the back-side of the card, for example the photo attached (just an idea) or some great design.
See flyer (attached) and harbor9studio.example for inspiration, maybe use of the photo of me (attached) in a circle or something

I´m very excited for your designs and thanks a lot in advance!! :)

Target Market(s)

Shops, hotels, shopping centers, etc. in Vienna, Austria

Industry/Entity Type

Business

Contact Information for Business Card

double-sided, use red of the logo, 360° vornix lanescope certified photographer

Font styles to use
Serif
Sans Serif

Colors
ec1f27

Requirements
Nice to have
• maybe some 360° design on back-side
• maybe include photo of me in a circle or something or sketched in red colour

```html
<!DOCTYPE html>
<html lang="en">
<head>
<meta charset="utf-8">
<title>Harbor9Studio – Business Card</title>
<link rel="stylesheet" href="https://fonts.googleapis.com/css2?family=Montserrat:wght@600;700&family=Open+Sans:wght@600;700&family=Roboto+Condensed:wght@300;700&display=swap">
<style>
  :root {
    --brand-red: #ec1f27;
    --brand-red-dark: #d8182a;
    --paper: #ffffff;
    --stage: #eeeff1;
    --grey-panel: #d3d4d6;
    --grey-stripe: #e6e7e8;
    --grey-text: #9a9b9e;
    --ink: #1d1d1f;
    --call-green: #1a8a3a;
    --photo-warm: #8a5a35;
    --photo-deep: #4a1e18;
  }
  * { box-sizing: border-box; margin: 0; padding: 0; }
  html, body { width: 1200px; height: 1006px; overflow: hidden; background: var(--stage); }
  .canvas { position: relative; width: 1200px; height: 1006px; }

  .card {
    position: absolute; left: 150px; width: 900px; height: 460px;
    background: var(--brand-red); padding: 22px;
    box-shadow: 0 6px 18px rgba(0,0,0,.12);
  }
  .card--front { top: 28px; }
  .card--back  { top: 518px; }
  .card__inner { position: relative; width: 100%; height: 100%; background: var(--paper); overflow: hidden; }

  /* Front */
  .front__photo-band {
    position: absolute; left: 0; top: 0; width: 100%; height: 180px;
    background: linear-gradient(110deg, var(--photo-deep) 0%, var(--photo-warm) 45%, #c9a27a 75%, #e2cdb0 100%);
  }
  .front__badge {
    position: absolute; right: 40px; top: 128px; width: 170px; height: 40px;
    border-radius: 6px; background: rgba(255,255,255,.85);
  }
  .front__portrait {
    position: absolute; left: 60px; top: 108px; width: 142px; height: 142px; border-radius: 50%;
    background: radial-gradient(circle at 50% 40%, #8d949a, #3c4147);
    border: 3px solid #222;
  }
  .front__name {
    position: absolute; left: 228px; top: 120px;
    font-family: "Montserrat", sans-serif; font-weight: 700; font-size: 38px; color: var(--paper);
    letter-spacing: .5px;
  }
  .front__contacts { position: absolute; left: 236px; top: 214px; list-style: none; }
  .contact { display: flex; align-items: center; gap: 18px; height: 50px; font-family: "Open Sans", sans-serif; font-weight: 600; font-size: 20px; color: var(--ink); }
  .contact__icon { width: 34px; height: 34px; flex: none; }

  /* Back */
  .back__shapes { position: absolute; inset: 0; }
  .back__brand { position: absolute; left: 30px; top: 156px; display: flex; align-items: center; gap: 14px; }
  .back__brand-mark { width: 50px; height: 50px; background: var(--brand-red-dark); }
  .back__brand-name { font-family: "Roboto Condensed", sans-serif; font-weight: 700; font-size: 46px; color: var(--grey-text); letter-spacing: -1px; }
  .back__phone {
    position: absolute; right: 48px; top: 266px;
    font-family: "Roboto Condensed", sans-serif; font-weight: 300; font-size: 46px; color: var(--paper);
  }
  .back__callback {
    position: absolute; right: 40px; top: 340px; display: flex; align-items: center; gap: 10px;
    font-family: "Open Sans", sans-serif; font-weight: 700; font-size: 15px;
  }
  .callback__sms { color: var(--brand-red); }
  .callback__or { font-family: "Montserrat", sans-serif; font-size: 26px; color: var(--ink); }
  .callback__back { color: var(--call-green); }
  .callback__icon { width: 30px; height: 30px; }
</style>
</head>
<body>
<main class="canvas">

  <section class="card card--front" aria-label="Business card front">
    <div class="card__inner">
      <div class="front__photo-band" role="img" aria-label="360° interior photograph of a cosy restaurant"></div>
      <div class="front__badge" role="img" aria-label="Vornix Gold badge"></div>
      <div class="front__portrait" role="img" aria-label="Portrait photo of Tobias Merland"></div>
      <h1 class="front__name">Tobias Merland</h1>
      <ul class="front__contacts">
        <li class="contact">
          <svg class="contact__icon" viewBox="0 0 34 34" aria-hidden="true">
            <circle cx="17" cy="17" r="17" fill="var(--brand-red)"/>
            <rect x="8" y="11" width="18" height="12" fill="none" stroke="#fff" stroke-width="2"/>
            <path d="M8 11 L17 18 L26 11" fill="none" stroke="#fff" stroke-width="2"/>
          </svg>
          <span>tobias@harbor9studio.example</span>
        </li>
        <li class="contact">
          <svg class="contact__icon" viewBox="0 0 34 34" aria-hidden="true">
            <circle cx="17" cy="17" r="17" fill="var(--brand-red)"/>
            <circle cx="17" cy="17" r="9" fill="none" stroke="#fff" stroke-width="1.8"/>
            <ellipse cx="17" cy="17" rx="4" ry="9" fill="none" stroke="#fff" stroke-width="1.5"/>
            <path d="M8 17 H26 M10 12 H24 M10 22 H24" stroke="#fff" stroke-width="1.3"/>
          </svg>
          <span>harbor9studio.example</span>
        </li>
      </ul>
    </div>
  </section>

  <section class="card card--back" aria-label="Business card back">
    <div class="card__inner">
      <svg class="back__shapes" viewBox="0 0 856 416" preserveAspectRatio="none" aria-hidden="true">
        <polygon points="0,0 462,0 262,416 0,416" fill="var(--paper)"/>
        <polygon points="462,0 500,0 300,416 262,416" fill="var(--grey-stripe)"/>
        <polygon points="500,0 856,0 856,416 300,416" fill="var(--grey-panel)"/>
        <polygon points="440,0 856,0 856,70 600,240" fill="var(--brand-red)"/>
      </svg>
      <div class="back__brand">
        <span class="back__brand-mark"></span>
        <span class="back__brand-name">Harbor9Studio</span>
      </div>
      <p class="back__phone">+49 160 55 82 907</p>
      <p class="back__callback">
        <span class="callback__sms">SEND US A SMS</span>
        <svg class="callback__icon" viewBox="0 0 30 30" aria-hidden="true">
          <rect x="3" y="7" width="24" height="16" fill="var(--brand-red)"/>
          <path d="M3 7 L15 17 L27 7" fill="none" stroke="#fff" stroke-width="2"/>
        </svg>
        <span class="callback__or">or</span>
        <svg class="callback__icon" viewBox="0 0 30 30" aria-hidden="true">
          <circle cx="15" cy="15" r="13" fill="var(--call-green)"/>
        </svg>
        <span class="callback__back">WE CALL YOU BACK</span>
      </p>
    </div>
  </section>

</main>
</body>
</html>
```